Visitenkarten-Design
Zielgruppe
Malerbetrieb
Zielgruppe: Private Haushalte, Hausverwaltungen
Aufgabenstellung
Logo ist vorhanden
Lorenz Dallmer
Malermeister

```html
<!DOCTYPE html>
<html lang="de">
<head>
<meta charset="utf-8">
<title>Visitenkarte Malerbetrieb Dallmer</title>
<link href="https://fonts.googleapis.com/css2?family=Fira+Sans+Condensed:wght@300;600&display=swap" rel="stylesheet">
<style>
  :root {
    --stage: #d0d0d0;
    --card: #ffffff;
    --ink: #222529;
    --cyan: #1fa0e0;
    --yellow: #fff200;
    --magenta: #c6077f;
  }
  * { margin: 0; padding: 0; box-sizing: border-box; }
  html, body { width: 1200px; height: 849px; overflow: hidden; }
  body { background: var(--stage); position: relative; font-family: "Fira Sans Condensed", sans-serif; color: var(--ink); }

  .card {
    position: absolute;
    top: 209px;
    width: 288px;
    height: 445px;
    background: var(--card);
    text-align: center;
  }
  .card--front { left: 196px; }
  .card--back { left: 705px; }

  .stripes { position: absolute; left: 0; width: 100%; top: 384px; }
  .stripe { display: block; height: 7px; width: 100%; margin-bottom: 5.5px; }
  .stripe--cyan { background: var(--cyan); }
  .stripe--yellow { background: var(--yellow); }
  .stripe--magenta { background: var(--magenta); }

  .brand {
    position: absolute;
    left: 0;
    width: 100%;
    top: 128px;
    font-weight: 600;
    font-size: 60px;
    line-height: 1;
    letter-spacing: 2px;
    color: var(--ink);
  }

  .contact { position: absolute; left: 0; width: 100%; font-size: 17px; line-height: 20.5px; }
  .contact__person { top: 61px; font-weight: 600; }
  .contact__address { top: 123px; font-weight: 300; }
  .contact__reach { top: 184px; font-weight: 300; }
  .contact__web { top: 350px; font-weight: 600; }
</style>
</head>
<body>
  <section class="card card--front">
    <div class="brand">DALLMER</div>
    <div class="stripes">
      <span class="stripe stripe--cyan"></span>
      <span class="stripe stripe--yellow"></span>
      <span class="stripe stripe--magenta"></span>
    </div>
  </section>

  <section class="card card--back">
    <p class="contact contact__person">Lorenz Dallmer<br>Malermeister</p>
    <p class="contact contact__address">Kastanienweg 17 c<br>24581 Lindenfeld</p>
    <p class="contact contact__reach">Tel: 0170 - 52 38 904<br>info@malereibetrieb-dallmer.de</p>
    <p class="contact contact__web">www.malereibetrieb-dallmer.de</p>
    <div class="stripes">
      <span class="stripe stripe--cyan"></span>
      <span class="stripe stripe--yellow"></span>
      <span class="stripe stripe--magenta"></span>
    </div>
  </section>
</body>
</html>
```